Brochure Design

We need a 6 page Brochure designed for our product, please see attached document for more information. The content should focus on account work.

Target Market(s)

Businesses that use a taxi service for their business

Requirements
Must have
• Must have key content on the services we provide for Account work

```html
<!DOCTYPE html>
<html lang="en">
<head>
<meta charset="utf-8">
<title>Cabora Account Brochure</title>
<link rel="stylesheet" href="https://fonts.googleapis.com/css2?family=Montserrat:wght@400;500;600;700&family=Lora:wght@400&display=swap">
<style>
:root{
  --stage:#d9d9d9;
  --paper:#efefef;
  --cover:#e6e6e6;
  --charcoal:#4a4a4a;
  --charcoal-dark:#333333;
  --yellow:#e8b523;
  --ink:#2b2b2b;
  --muted:#8a8a8a;
  --light-text:#d6d6d6;
}
*{margin:0;padding:0;box-sizing:border-box}
html,body{width:1200px;height:810px;overflow:hidden;background:var(--stage)}
body{font-family:"Montserrat",sans-serif;position:relative}
.brochure{position:absolute;left:60px;top:225px;width:1080px;height:360px;display:flex;box-shadow:0 10px 30px rgba(0,0,0,.18)}
.panel{position:relative;width:360px;height:360px;overflow:hidden}
.panel svg.shapes{position:absolute;inset:0}

/* left panel */
.panel--features{background:var(--paper);display:flex;flex-direction:column;align-items:center;justify-content:center;gap:30px;padding:0 80px}
.feature{display:flex;flex-direction:column;align-items:center;text-align:center;gap:8px}
.feature svg{width:26px;height:26px}
.feature p{font-size:8px;line-height:1.45;color:var(--muted)}

/* middle panel */
.panel--services{background:var(--charcoal)}
.service{position:absolute;left:100px;width:240px}
.service h3{font-size:9.5px;font-weight:600;color:#fff;letter-spacing:.3px;text-transform:uppercase}
.service p{font-size:7.5px;line-height:1.4;color:var(--light-text);margin-top:3px}
.offices{position:absolute;left:100px;top:220px;width:240px;display:flex;justify-content:space-between}
.office h4{font-size:7px;font-weight:700;color:#fff;text-transform:uppercase}
.office p{font-size:6.5px;line-height:1.45;color:var(--light-text)}
.office + .office{margin-top:44px}
.enquiries{position:absolute;left:100px;top:280px}
.enquiries h4{font-size:7px;font-weight:700;color:#fff;text-transform:uppercase}
.enquiries p{font-size:6.5px;color:var(--light-text)}
.website{position:absolute;left:0;right:0;bottom:22px;text-align:center;font-size:8px;letter-spacing:3px;color:var(--yellow);font-weight:600;padding-left:60px}

/* cover */
.panel--cover{background:var(--cover)}
.cover-badge{position:absolute;left:165px;top:150px;width:120px;text-align:center;color:var(--ink)}
.brand{display:inline-flex;align-items:center;gap:5px;font-family:"Montserrat",sans-serif;font-weight:700;font-size:15px;color:var(--ink)}
.brand-dot{width:9px;height:9px;border-radius:50%;background:var(--ink)}
.tagline{font-family:"Lora",serif;font-size:14px;line-height:1.2;margin-top:8px}
</style>
</head>
<body>
<main class="brochure">

  <section class="panel panel--features">
    <div class="feature">
      <svg viewBox="0 0 24 24" fill="none" stroke="#555" stroke-width="1.4" stroke-linecap="round"><path d="M10 14a4 4 0 0 0 5.7 0l3-3a4 4 0 0 0-5.7-5.7l-1 1"/><path d="M14 10a4 4 0 0 0-5.7 0l-3 3a4 4 0 0 0 5.7 5.7l1-1"/></svg>
      <p>Safety features where a passenger can send a link to any contact for them to track the ride real time.</p>
    </div>
    <div class="feature">
      <svg viewBox="0 0 24 24" fill="none" stroke="#555" stroke-width="1.4"><rect x="5" y="11" width="14" height="10" rx="1.5"/><path d="M8 11V8a4 4 0 0 1 8 0v3"/><circle cx="12" cy="16" r="1.2"/></svg>
      <p>Drivers thoroughly vetted including the enhanced disclosure and barring system, ensuring the highest level of safety checks available for the passengers.</p>
    </div>
    <div class="feature">
      <svg viewBox="0 0 24 24" fill="none" stroke="#555" stroke-width="1.4"><path d="M2 12s4-6 10-6 10 6 10 6-4 6-10 6S2 12 2 12z"/><circle cx="12" cy="12" r="3"/></svg>
      <p>Customer benefits as there is no surge pricing.</p>
    </div>
  </section>

  <section class="panel panel--services">
    <svg class="shapes" viewBox="0 0 360 360">
      <rect x="0" y="30" width="50" height="290" fill="var(--yellow)"/>
      <polygon points="27,60 41,36 69,36 83,60 69,84 41,84" fill="var(--yellow)"/>
      <polygon points="27,112 41,88 69,88 83,112 69,136 41,136" fill="var(--yellow)"/>
      <polygon points="27,166 41,142 69,142 83,166 69,190 41,190" fill="var(--yellow)"/>
      <g fill="none" stroke="var(--charcoal-dark)" stroke-width="1.4" stroke-linecap="round" stroke-linejoin="round">
        <path d="M47 52c0 9 7 16 16 16l2-4-4-2-2 2c-3-1-5-3-6-6l2-2-2-4z"/>
        <path d="M55 102a6 6 0 0 1 6 6c0 5-6 11-6 11s-6-6-6-11a6 6 0 0 1 6-6z"/><circle cx="55" cy="108" r="2"/>
        <path d="M44 170h22v-5l-3-5H47l-3 5z"/><circle cx="49" cy="171" r="2"/><circle cx="61" cy="171" r="2"/><path d="M52 158h6"/>
      </g>
    </svg>
    <div class="service" style="top:48px">
      <h3>24/7 Support</h3>
      <p>Our Account Management Team, and support 24/7/365 from our HQ in London.</p>
    </div>
    <div class="service" style="top:100px">
      <h3>Average 7 Min Pick Ups</h3>
      <p>Benefits from a priority service, ensuring we're only ever moments away.</p>
    </div>
    <div class="service" style="top:154px">
      <h3>Trained, Hand Picked Drivers</h3>
      <p>Our drivers are trained and vetted to ensure high service, quality and safety.</p>
    </div>
    <div class="offices">
      <div class="office">
        <h4>Head Office - UK</h4>
        <p>Cabora Mobility Ltd<br>Unit 4 Meridian Court<br>Elm Row, Northbridge<br>NB4 7QS</p>
      </div>
      <div class="office">
        <h4>Canada</h4>
        <p>88 Larchmont Avenue<br>Ridgeview, Ontario<br>K2P 0X4<br>Tel: +1 (555) 014 2290</p>
      </div>
    </div>
    <div class="enquiries">
      <h4>General Enquiries</h4>
      <p>hello@cabora.example</p>
    </div>
    <p class="website">WWW.CABORA.EXAMPLE</p>
  </section>

  <section class="panel panel--cover">
    <svg class="shapes" viewBox="0 0 360 360">
      <defs>
        <linearGradient id="photoTone" x1="0" y1="0" x2="1" y2="1">
          <stop offset="0" stop-color="#b8a77a"/>
          <stop offset=".45" stop-color="#8d9088"/>
          <stop offset="1" stop-color="#2f4a3a"/>
        </linearGradient>
      </defs>
      <polygon points="0,0 195,0 255,125 175,300 0,300" fill="url(#photoTone)" role="img" aria-label="Photo of a hand holding a smartphone with a taxi booking app, a blurred taxi behind"/>
      <polygon points="100,300 130,245 235,245 265,300 235,360 130,360" fill="var(--charcoal-dark)"/>
      <polygon points="145,205 185,136 265,136 305,205 265,274 185,274" fill="var(--yellow)"/>
      <polygon points="277,105 291,81 319,81 333,105 319,129 291,129" fill="#3d3d3d"/>
    </svg>
    <div class="cover-badge">
      <span class="brand"><span class="brand-dot"></span>Cabora</span>
      <p class="tagline">Your Safety is our Priority!</p>
    </div>
  </section>

</main>
</body>
</html>
```